Outdoor group fitness training - Greta Moxley Personal Training

I want an eye catching A4 flyer that promotes my two outdoor fitness groups. I have uploaded photos of each location: Mylor and Pasadena.
The target group is existing and potential new Personal training clients - all adults. There are two morning groups at Mylor ; one evening and one morning group at Pasadena. The groups will be for up to 8 people and are for all fitness levels.I want to encourage people to come and have a go. I have also uploaded a design I have used through printhollow for a previous flyer. I would like to use the orange graphic of the two people at the bottom of this design.
Cost is $15 per person
Location and times - Brackenridge Oval Wednesdays 7.30am; Sundays 8am
Corvale High School Thursdays 6.30pm: Saturdays 8am
Updates

Thanks so much to all of you for submitting a great set of designs. it was really hard making a choice in the end, and I really appreciate the promptness and creativity that went into the designs. I will certainly keep you in mind for future jobs. Cheers and have a great day Greta Moxley

Target Market(s)

40 - 60 year old adults: cross section of professionals, tradespeople and retirees. People who will enjoy socialising while also getting fit. No extremely fit people - cross section of beginners to intermediate; males and females

Industry/Entity Type

Training

Font styles to use
Sans Serif

Colors
f78f20
9bcb3c
ecf7fb

Requirements
Must have
• Fast turnaround required - within two days
Bright and attention grabbing, engaging. Could be A4 or could be postcard size?

State cost clearly
State that first 5 people to join either group will get first session at half price

```html
<!DOCTYPE html>
<html lang="en">
<head>
<meta charset="utf-8">
<title>Greta Moxley Personal Training – Outdoor Fitness Groups</title>
<link rel="stylesheet" href="https://fonts.googleapis.com/css2?family=Arimo:ital,wght@0,400;0,700;1,700&display=swap">
<style>
  :root {
    --orange: #f78f20;
    --orange-deep: #f5862f;
    --green: #a6ce47;
    --green-text: #9bcb3c;
    --white: #ffffff;
    --black: #000000;
    --ink: #111111;
    --backdrop: #ecf7fb;
  }
  * { margin: 0; padding: 0; box-sizing: border-box; }
  html, body {
    width: 889px;
    height: 1200px;
    overflow: hidden;
    background: var(--backdrop);
    font-family: "Arimo", Arial, sans-serif;
  }
  .flyer {
    position: absolute;
    left: 14px;
    top: 10px;
    width: 860px;
    height: 1179px;
    background: var(--white);
    overflow: hidden;
  }
  .trainer-name {
    position: absolute;
    right: 89px;
    top: 70px;
    font-size: 46px;
    font-weight: 700;
    font-style: italic;
    color: var(--orange);
    letter-spacing: 0.3px;
  }
  .location {
    position: absolute;
    left: 88px;
    width: 683px;
    height: 204px;
    display: flex;
  }
  .location--corvale { top: 158px; }
  .location--brackenridge { top: 398px; }
  .location__photo {
    width: 363px;
    height: 100%;
  }
  .location--corvale .location__photo {
    background: linear-gradient(180deg, #b9d3e6 0%, #6f8a5a 30%, #4d6a35 55%, #7c8a4a 75%, #55534c 100%);
  }
  .location--brackenridge .location__photo {
    background: linear-gradient(180deg, #c8dcea 0%, #4f7a3b 25%, #5f8c42 45%, #8d8c80 65%, #a9a49a 100%);
  }
  .location__info {
    flex: 1;
    padding: 24px 0 0 28px;
    color: var(--white);
  }
  .location--corvale .location__info { background: var(--orange-deep); }
  .location--brackenridge .location__info { background: var(--green); padding-top: 38px; }
  .location__name {
    font-size: 29px;
    font-weight: 700;
    line-height: 1.17;
    text-transform: uppercase;
  }
  .schedule {
    margin-top: 14px;
    display: grid;
    grid-template-columns: auto auto;
    justify-content: start;
    column-gap: 10px;
    row-gap: 8px;
    font-size: 24px;
    font-weight: 700;
    color: var(--ink);
  }
  .location--brackenridge .schedule { margin-top: 28px; column-gap: 8px; }
  .action-photo {
    position: absolute;
    left: 0;
    top: 656px;
    width: 860px;
    height: 496px;
    background:
      radial-gradient(ellipse at 85% 15%, #e9ddd0 0%, rgba(233,221,208,0) 45%),
      linear-gradient(100deg, #6e3a22 0%, #8d4e2c 25%, #b27751 45%, #c9a489 65%, #b06a43 85%, #8a4628 100%);
  }
  .price-badge {
    position: absolute;
    left: 63px;
    top: 790px;
    width: 242px;
    height: 242px;
  }
  .price-badge svg { position: absolute; inset: 0; }
  .price-badge__amount {
    position: absolute;
    left: 0;
    width: 100%;
    top: 70px;
    text-align: center;
    color: var(--orange);
    font-weight: 700;
    line-height: 1;
  }
  .price-badge__currency { font-size: 50px; font-weight: 400; vertical-align: 8px; }
  .price-badge__number { font-size: 86px; letter-spacing: -2px; }
  .price-badge__unit {
    position: absolute;
    left: 0;
    width: 100%;
    top: 178px;
    text-align: center;
    font-size: 15px;
    font-weight: 700;
    color: var(--green-text);
  }
  .offer {
    position: absolute;
    left: 73px;
    top: 1040px;
    font-size: 20px;
    font-weight: 700;
    line-height: 27px;
    color: var(--white);
    text-transform: uppercase;
  }
  .footer-band {
    position: absolute;
    left: 0;
    top: 1152px;
    width: 860px;
    height: 27px;
    background: var(--black);
    color: var(--orange);
    font-size: 18.5px;
    font-weight: 700;
    line-height: 27px;
    text-align: center;
    text-transform: uppercase;
    white-space: nowrap;
  }
</style>
</head>
<body>
  <main class="flyer">
    <h1 class="trainer-name">Greta Moxley</h1>

    <section class="location location--corvale">
      <div class="location__photo" role="img" aria-label="Photo of the Corvale High School grounds: lawn, trees and a footpath"></div>
      <div class="location__info">
        <h2 class="location__name">Corvale<br>High School</h2>
        <div class="schedule">
          <span>Thursdays</span><span>6.30pm</span>
          <span>Saturdays</span><span>8.00am</span>
        </div>
      </div>
    </section>

    <section class="location location--brackenridge">
      <div class="location__photo" role="img" aria-label="Photo of Brackenridge Oval: clubhouse, gravel path, grass and trees"></div>
      <div class="location__info">
        <h2 class="location__name">Brackenridge Oval</h2>
        <div class="schedule">
          <span>Wednesdays</span><span>7.30am</span>
          <span>Sundays</span><span>8.00am</span>
        </div>
      </div>
    </section>

    <div class="action-photo" role="img" aria-label="Orange-toned photo of two people jogging along a waterfront path"></div>

    <div class="price-badge">
      <svg viewBox="0 0 242 242" width="242" height="242" aria-hidden="true">
        <polygon fill="#000" points="121,0 142.1,28.4 173.5,12 180.2,46.7 215.6,45.6 206.6,79.8 239,94.1 216,121 239,147.9 206.6,162.2 215.6,196.4 180.2,195.3 173.5,230 142.1,213.6 121,242 99.9,213.6 68.5,230 61.8,195.3 26.4,196.4 35.4,162.2 3,147.9 26,121 3,94.1 35.4,79.8 26.4,45.6 61.8,46.7 68.5,12 99.9,28.4"/>
      </svg>
      <div class="price-badge__amount"><span class="price-badge__currency">$</span><span class="price-badge__number">15</span></div>
      <div class="price-badge__unit">PER PERSON</div>
    </div>

    <p class="offer">First 5 people to<br>join either group<br>will get first session<br>at half price</p>

    <footer class="footer-band">Groups will be for up to 8 people and are for all fitness levels</footer>
  </main>
</body>
</html>
```